Law Firm Website

I currently have a temporary site that I created myself at www.kbrandellegal.net (hosted by hostpivot). I am generally happy with the content.

My permanent website just has basic information right now: www.kbrandellegal.com (hosted by cloudperch). I want to take the general content from the temporary website and have a more professional looking website on the permanent website. I want it in Wordpress format. I want a link to my blog: www.rivetsand.com. I want it to work on pads and smart phones. My number and e-mail address should be available on every page. The idea is to feature the potential client more than the lawyer.
Updates

Several of the designs are good. I would like the front page to have my number and address at the top (and at the top of every page) and to identify my law firm as "Law Office of Karen J. Brandell". No need to include "kbrandellegal" as that is just the web address. I like showing the most recent blog posts on the front page. I don't need video. No need to emphasize office hours or map location on the front page (that could be under a contact button). My picture should be somewhere. I would like an image from Boston on the front page if we can find one that is not copyright protected. No images of gavels or scales of justice. See some of the sample websites I listed in previous messages. Thanks!

Reason: I need more time to evaluate designs.

Reason: Designers apparently misunderstood and provided design that was not wordpress.

Industry/Entity Type

Law Firm

```html
<!DOCTYPE html>
<html lang="en">
<head>
<meta charset="utf-8">
<title>Law Office of Karen J. Brandell</title>
<link rel="stylesheet" href="https://fonts.googleapis.com/css2?family=Nunito+Sans:wght@400;600&display=swap">
<style>
:root{
  --ink:#333333;
  --ink-soft:#555555;
  --nav-bg:#2b2b2b;
  --nav-active:#3b3b3b;
  --rule:#d8d8d8;
  --tag-bg:#e6e6e6;
  --btn-top:#f4f4f4;
  --btn-bottom:#d6d6d6;
  --white:#ffffff;
}
*{box-sizing:border-box;margin:0;padding:0}
html,body{width:1040px;height:1200px;overflow:hidden;background:var(--white)}
body{font-family:"Nunito Sans",Arial,sans-serif;color:var(--ink)}
.page{position:relative;width:1200px;height:1384px;transform:scale(.866667);transform-origin:0 0}
.abs{position:absolute}

/* header */
.brand-name{left:130px;top:16px;font-size:30px;color:#222;letter-spacing:.2px}
.brand-rule{left:128px;top:55px;width:218px;height:1px;background:#555}
.brand-sub{left:143px;top:60px;font-size:14px;color:#666}
.call{left:866px;top:33px;font-size:18px;color:#222}

/* nav */
.main-nav{left:0;top:92px;width:1200px;height:53px;background:var(--nav-bg)}
.nav-list{display:flex;list-style:none;position:absolute;left:109px;top:0;height:53px}
.nav-list li{height:53px;line-height:53px;padding:0 14.5px;font-size:14px;color:var(--white)}
.nav-list li.active{background:var(--nav-active);padding:0 17px}

/* hero */
.hero{left:0;top:145px;width:1200px;height:432px;overflow:hidden;
  background:radial-gradient(ellipse at 75% 40%,#f3b060 0%,#c8701f 35%,#7a3a10 75%,#4a2208 100%)}
.hero-panel{left:0;top:0}
.hero-copy{left:128px;top:55px;color:var(--white);font-size:17px;line-height:28px;width:400px}
.hero-copy .big{font-size:23px}
.hero-copy .huge{font-size:27px}
.learn{left:126px;top:215px;width:134px;height:41px;background:#f2f2f2;border-radius:3px;
  font-size:16px;line-height:41px;text-align:center;color:#222}
.portrait{left:105px;top:275px;width:140px;height:140px;border-radius:50%;
  background:linear-gradient(160deg,#9aa7b6,#3d4a5c);border:3px solid rgba(255,255,255,.35)}
.name-card{left:230px;top:297px;width:282px;height:97px;background:rgba(255,255,255,.28)}
.name-card .n{position:absolute;left:38px;top:12px;font-size:27px;color:#222}
.name-card .r{position:absolute;left:38px;top:48px;width:217px;height:1px;background:#444}
.name-card .s{position:absolute;left:40px;top:53px;font-size:13px;color:#333}
.dots{left:870px;top:380px;display:flex;gap:7px}
.dots span{width:14px;height:14px;background:#111}
.dots span.off{background:#6b5a4a}

/* welcome */
.office-photo{left:132px;top:611px;width:254px;height:165px;
  background:linear-gradient(90deg,#b9c3c9,#e6ecef 50%,#a7b2b9)}
.h2{font-size:19px;color:#333;text-transform:uppercase;font-weight:400}
.h2-rule{height:1px;background:var(--rule)}
.body-text{font-size:13px;line-height:15.5px;color:#444}
.btn{height:28px;line-height:28px;text-align:center;font-size:13px;color:#444;border-radius:3px;
  background:linear-gradient(var(--btn-top),var(--btn-bottom))}
.contact-text{left:832px;top:634px;font-size:13px;line-height:18px;color:#444}

/* blog */
.rule{height:1px;background:var(--rule)}
.vrule{width:1px;background:var(--rule)}
.post{top:888px;width:305px}
.post h3{font-size:15px;line-height:24px;font-weight:400;text-transform:uppercase;color:#333}
.post .tag{display:inline-block;margin-top:8px;background:var(--tag-bg);padding:0 10px 0 6px;height:27px;line-height:27px;font-size:13px;color:#444}
.post p{margin-top:16px;font-size:13px;line-height:18px;color:#444}
.post .btn{width:89px;margin-top:17px}

/* newsletter */
.news-title{left:204px;top:1175px;font-size:25px;color:#333}
.email{left:518px;top:1167px;width:295px;height:43px;border:1px solid #ddd;border-radius:3px;
  font-size:14px;line-height:43px;padding-left:14px;color:#333}
.subscribe{left:821px;top:1168px;width:133px;height:41px;line-height:41px;font-size:16px;color:#333}

/* footer */
.foot-nav{left:109px;top:1255px;display:flex;list-style:none}
.foot-nav li{padding:0 14.5px;font-size:14px;line-height:26px;color:#333}
.foot-nav li:first-child{padding:0 17px}
.social{left:503px;top:1297px}
.copy{left:0;top:1346px;width:1200px;text-align:center;font-size:13px;color:#333}
</style>
</head>
<body>
<div class="page">

  <header>
    <div class="abs brand-name">Karen J. Brandell</div>
    <div class="abs brand-rule"></div>
    <div class="abs brand-sub">Law Office of Karen J. Brandell</div>
    <div class="abs call">CALL US : 617 555-0142</div>
  </header>

  <nav class="abs main-nav">
    <ul class="nav-list">
      <li class="active">Home</li><li>Why Hire Me?</li><li>Success Stories</li><li>Practice Areas</li>
      <li>Representative Clients</li><li>Services Provided</li><li>Contact Us</li><li>How to Find Us</li>
    </ul>
  </nav>

  <section class="abs hero" role="img" aria-label="Warm-toned photo of brass scales on a wooden desk">
    <svg class="abs hero-panel" width="1200" height="432" aria-hidden="true">
      <polygon points="0,38 460,38 605,268 0,268" fill="rgba(40,22,10,.55)"/>
    </svg>
    <div class="abs hero-copy">
      <div><span class="huge">Protecting</span> and Defending</div>
      <div><span class="huge">Your Business</span> Against Competitors,</div>
      <div class="big">Rogue Employees, Cheating Business</div>
      <div><span class="big">Partners,</span> Devious Contracting Parties,</div>
      <div><span class="big">and Overzealous</span> Government Agencies.</div>
    </div>
    <div class="abs learn">LEARN MORE</div>
    <div class="abs portrait" role="img" aria-label="Portrait photo of the attorney"></div>
    <div class="abs name-card">
      <div class="n">Karen J. Brandell</div>
      <div class="r"></div>
      <div class="s">Law Office of Karen J. Brandell</div>
    </div>
    <div class="abs dots"><span></span><span></span><span></span><span class="off"></span></div>
  </section>

  <section class="welcome">
    <div class="abs office-photo" role="img" aria-label="Photo of three business people walking in an office corridor"></div>
    <h2 class="abs h2" style="left:403px;top:603px">Welcome to our website</h2>
    <div class="abs h2-rule" style="left:403px;top:630px;width:260px"></div>
    <div class="abs body-text" style="left:404px;top:639px;width:390px">
      <p>Your business is under constant attack. With more success, you become more of a target. Whether it's keeping you out of a lawsuit or defending one that you are already in (or prosecuting one when necessary), I'm here to help.</p>
      <p style="margin-top:15px">Don't settle for lawyers who promise to work to solve your problems. I will work to prevent your problems in the first place. Learn more about litigation avoidance in my practice areas of law.</p>
    </div>
    <div class="abs btn" style="left:687px;top:783px;width:89px">Readmore</div>

    <h2 class="abs h2" style="left:830px;top:603px">Contact us</h2>
    <div class="abs h2-rule" style="left:830px;top:630px;width:160px"></div>
    <div class="abs contact-text">
      Address : 48 Harlow St. 3rd Floor<br>
      <span style="padding-left:58px">Boston, MA 02111.</span><br><br>
      Phone: 617 555-0142<br>
      Fax: 857 555-0197<br><br>
      Email: kbrandell@kbrandellegal.com<br>
      Blog : www.rivetsand.com
    </div>
  </section>

  <div class="abs rule" style="left:120px;top:826px;width:960px"></div>

  <section class="blog">
    <h2 class="abs h2" style="left:125px;top:838px">My Blog</h2>
    <div class="abs h2-rule" style="left:125px;top:872px;width:88px"></div>
    <div class="abs vrule" style="left:441px;top:848px;height:288px"></div>
    <div class="abs vrule" style="left:762px;top:848px;height:288px"></div>

    <article class="abs post" style="left:124px">
      <h3>You're damned if you don't respond appropriately to a poor Rateline review or online post.</h3>
      <span class="tag" style="margin-left:-4px">Posted: January 15, 2014 in Lawsuits</span>
      <p>We live in crazy times for businesses. Any crackpot with a computer and internet connection can say anything that they want about your business in an online review, on social media, etc.</p>
      <div class="btn">Readmore</div>
    </article>
    <article class="abs post" style="left:455px">
      <h3>You're damned if you don't respond appropriately to a poor Rateline review or online post.</h3>
      <span class="tag" style="margin-left:-4px">Posted: January 15, 2014 in Lawsuits</span>
      <p>We live in crazy times for businesses. Any crackpot with a computer and internet connection can say anything that they want about your business in an online review, on social media, etc.</p>
      <div class="btn">Readmore</div>
    </article>
    <article class="abs post" style="left:778px">
      <h3>You're damned if you don't respond appropriately to a poor Rateline review or online post.</h3>
      <span class="tag" style="margin-left:-6px">Posted: January 15, 2014 in Lawsuits</span>
      <p>We live in crazy times for businesses. Any crackpot with a computer and internet connection can say anything that they want about your business in an online review, on social media, etc.</p>
      <div class="btn">Readmore</div>
    </article>
  </section>

  <div class="abs rule" style="left:120px;top:1147px;width:960px"></div>

  <section class="newsletter">
    <div class="abs news-title">NEWSLETTER SUBSCRIBE</div>
    <div class="abs email">Email id</div>
    <div class="abs btn subscribe">SUBSCRIBE</div>
  </section>

  <div class="abs rule" style="left:120px;top:1237px;width:960px"></div>

  <footer>
    <ul class="abs foot-nav">
      <li>Home</li><li>Why Hire Me?</li><li>Success Stories</li><li>Practice Areas</li>
      <li>Representative Clients</li><li>Services Provided</li><li>Contact Us</li><li>How to Find Us</li>
    </ul>
    <svg class="abs social" width="196" height="34" role="img" aria-label="Social media links">
      <defs>
        <linearGradient id="soc" x1="0" y1="0" x2="0" y2="1">
          <stop offset="0" stop-color="#f6f6f6"/><stop offset="1" stop-color="#d2d2d2"/>
        </linearGradient>
      </defs>
      <circle cx="17" cy="17" r="16" fill="url(#soc)" stroke="#bbb"/>
      <circle cx="57" cy="17" r="16" fill="url(#soc)" stroke="#bbb"/>
      <circle cx="97" cy="17" r="16" fill="url(#soc)" stroke="#bbb"/>
      <circle cx="137" cy="17" r="16" fill="url(#soc)" stroke="#bbb"/>
      <circle cx="177" cy="17" r="16" fill="url(#soc)" stroke="#bbb"/>
    </svg>
    <div class="abs copy">© 2014.www.companyname.com</div>
  </footer>

</div>
</body>
</html>
```